1. Can you describe what your company does?
-> We at R and P Orvex, we do Tube bending and its subassemblies. We can cater to different materials like Mild Steel, Stainless Steel, Aluminium and other non-ferrous material. We collaborate with our clients to make precise components to meet their industry requirements. At R&P Orvex we cater to smaller batches or high-volume requirements as per project needs.

2. Who are your target customers for the website?
-> Automotive, Road construction, warehouse equipment, Data centers, beverage equipment industry, electronics products manufacturers for making fixtures.
-> customers which require tubes and pipe bending, exhaust pipes, sheet metal parts

3. Do you have an existing domain name / website address?
-> This was an existing site: https://www.randporvex.co.in/industry
-> using design.com I created this: https://kitpage.site/RandPOrvexpvtltd
But I am not very satisfied with the one I have created using design.com

4. In addition to a Home Page, which other pages / sections would you like your website to have:
About Us
Contact Us
Products / Services
Office / Mailing Address
Terms and Conditions

For each of the pages / sections you’d like to have, please provide the text (and images, if available) you would like to include.
-> Can you use the content that I have added on design.com : https://kitpage.site/RandPOrvexpvtltd

5. Which of the below are features and functionalities your website will need:
Image Gallery
Videos
Contact Form

6. Please provide the URLs for the social media profiles you'd like to link to the website.
-> Don't have one yet.

```html
<!DOCTYPE html>
<html lang="en">
<head>
<meta charset="utf-8">
<title>R and P Orvex — Tube Bending &amp; Subassemblies</title>
<link rel="stylesheet" href="https://fonts.googleapis.com/css2?family=Poppins:wght@400;500;600;700&display=swap">
<style>
:root{
  --blue:#2f56a6;
  --blue-dark:#24479a;
  --blue-deep:#1e3d86;
  --grey:#8b8b8b;
  --grey-dark:#6f6f6f;
  --ink:#1f1f1f;
  --muted:#444;
  --soft:#f0f2f7;
  --white:#fff;
}
*{box-sizing:border-box;margin:0;padding:0}
html,body{width:1200px;height:4847px;overflow:hidden;background:var(--white)}
body{font-family:"Poppins",sans-serif;color:var(--ink)}
.canvas{position:relative;width:1200px;height:4847px;overflow:hidden}
.abs{position:absolute}
.ph{position:absolute;display:block}
.center{text-align:center;left:0;width:1200px}

/* top bar & nav */
.topbar{top:0;left:0;width:1200px;height:45px}
.topbar-text{color:var(--white);font-size:15px;font-weight:600;top:11px}
.nav-link{top:70px;font-size:16px;font-weight:500;color:#222}
.nav-link.is-active{color:var(--blue)}
.brand{top:18px;left:500px;width:200px;text-align:center}
.brand-mark{display:block;width:44px;height:44px;border-radius:50%;background:var(--blue);margin:0 auto 6px}
.brand-name{font-size:14px;font-weight:500;color:var(--blue)}

/* hero */
.hero-photo{top:117px;left:0;width:1200px;height:598px;background:linear-gradient(110deg,#101010 0%,#2a2a2a 40%,#4a4540 62%,#8a6a3a 70%,#3a3835 85%,#222 100%)}
.hero-title{top:222px;left:98px;color:var(--white);font-size:44px;font-weight:700;line-height:52px}
.hero-text{top:338px;left:101px;width:410px;color:var(--white);font-size:14px;line-height:22.5px}
.btn{position:absolute;display:flex;align-items:center;justify-content:center;background:var(--blue);color:var(--white);font-weight:600;font-size:16px;border-radius:3px}
.btn-hex{position:absolute;right:-14px;top:50%;transform:translateY(-50%)}

/* about */
.about-band{top:1113px;left:0;width:1200px;height:853px;background:linear-gradient(180deg,#3258a8 0%,#2a4f9c 50%,#3459a5 100%)}
.about-card{top:828px;left:111px;width:978px;height:511px;background:var(--white);border-radius:14px;box-shadow:0 6px 24px rgba(0,0,0,.12);overflow:hidden}
.about-photo{top:0;left:0;width:490px;height:511px;background:linear-gradient(160deg,#4d6a86 0%,#7f94a6 45%,#3b4f63 100%)}
.about-title{top:905px;left:649px;font-size:34px;font-weight:600;color:var(--blue)}
.about-sub{top:958px;left:649px;width:330px;font-size:19px;line-height:27px;color:#222}
.about-tag{top:1019px;left:649px;font-size:15px;font-weight:500}
.about-text{top:1053px;left:649px;width:400px;font-size:14px;line-height:26px;color:var(--muted)}

/* services */
.section-title{font-size:35px;font-weight:400}
.section-title b{font-weight:700}
.services-title{top:1440px;color:var(--white)}
.services-text{top:1521px;color:var(--white);font-size:15px;line-height:24px}
.service{top:1612px;width:240px;text-align:center;color:var(--white)}
.service-name{font-size:17px;font-weight:500;margin-top:22px}
.service-text{font-size:14px;line-height:22.5px;margin-top:6px;opacity:.95}

/* products */
.products-title{top:2040px;left:111px;font-size:34px;font-weight:600}
.title-rule{position:absolute;background:var(--blue);height:5px}
.product-card{top:2129px;left:111px;width:651px;height:401px;border:3px solid #b9b9b9;border-radius:10px;background:#f7f7f7}
.product-img{top:2150px;width:299px;height:297px;border-radius:8px}
.product-name{top:2466px;width:299px;text-align:center;font-size:20px;font-weight:500}
.product-tab{top:2129px;width:94px;height:401px;background:var(--grey);border-radius:10px;display:flex;align-items:center;justify-content:center}
.product-tab span{transform:rotate(-90deg);white-space:nowrap;color:var(--white);font-weight:700;font-size:24px}

/* industries */
.industries{top:2648px;left:0;width:1200px;height:634px;background:var(--soft)}
.industries-title{top:2726px}
.industry{top:2816px;width:222px;height:297px;background:var(--white);box-shadow:0 3px 10px rgba(0,0,0,.08)}
.industry.is-open{height:359px;border:2px solid #a9a9a9;border-radius:6px}
.industry-img{top:0;left:0;width:100%;height:190px}
.industry-icon{position:absolute;top:158px;left:50%;margin-left:-32px;width:64px;height:64px;border-radius:50%;border:4px solid var(--white);display:flex;align-items:center;justify-content:center}
.industry-name{position:absolute;top:236px;left:0;width:100%;text-align:center;font-size:15px;font-weight:600;line-height:22px}
.industry-text{position:absolute;top:296px;left:10px;right:10px;text-align:center;font-size:13px;line-height:22px;color:#333}
.industry-rule{position:absolute;left:48px;right:48px;bottom:0;height:3px;background:var(--blue)}

/* gallery */
.gallery-title{top:3358px}
.gallery-img{top:3440px;height:320px}
.gallery-arrow{position:absolute;top:3567px;width:60px;height:60px;border-radius:50%;background:var(--white);box-shadow:0 2px 8px rgba(0,0,0,.2);display:flex;align-items:center;justify-content:center}

/* contact */
.contact-bg{top:3880px;left:0;width:1200px;height:527px;background:linear-gradient(180deg,#e9eaec 0%,#dcdee2 100%)}
.contact-title{top:3944px}
.field{position:absolute;background:var(--white);font-size:15px;color:#222;padding:14px 18px}
.submit{top:4247px;left:111px;width:461px;height:51px;font-size:17px;font-weight:700;border-radius:2px}

/* footer */
.footer-brand{top:4655px;left:111px;font-size:23px;color:var(--blue)}
.footer-mark{top:4510px;left:150px;width:90px;height:90px;border-radius:50%;border:4px solid var(--blue)}
.footer-head{top:4494px;font-size:19px;font-weight:600}
.footer-link{font-size:13.5px;color:#222}
.contact-item{display:flex;align-items:center;gap:14px;font-size:14px}
.contact-dot{width:38px;height:38px;border-radius:50%;background:var(--blue);display:flex;align-items:center;justify-content:center}
.news-text{top:4544px;left:864px;width:300px;font-size:14px;line-height:30px}
.news-email{top:4614px;left:866px;font-size:14px}
.news-line{top:4644px;left:863px;width:274px;height:1.5px;background:#999}
.subscribe{top:4674px;left:865px;width:156px;height:51px;font-size:16px;font-weight:700}
.footer-rule{top:4778px;left:120px;width:958px;height:1px;background:#bbb}
.copyright{top:4798px;font-size:14px;color:#333}
</style>
</head>
<body>
<div class="canvas">

  <!-- top bar -->
  <svg class="abs topbar" width="1200" height="45" viewBox="0 0 1200 45" aria-hidden="true">
    <polygon points="0,0 508,0 478,45 0,45" fill="var(--blue)"/>
    <polygon points="686,0 1200,0 1200,45 716,45" fill="var(--grey)"/>
  </svg>
  <svg class="abs" style="top:14px;left:120px" width="16" height="16" viewBox="0 0 24 24" aria-hidden="true"><path d="M6.6 10.8a15 15 0 0 0 6.6 6.6l2.2-2.2a1 1 0 0 1 1-.25 11.4 11.4 0 0 0 3.6.6 1 1 0 0 1 1 1V20a1 1 0 0 1-1 1A17 17 0 0 1 3 4a1 1 0 0 1 1-1h3.5a1 1 0 0 1 1 1c0 1.25.2 2.45.6 3.6a1 1 0 0 1-.25 1z" fill="#fff"/></svg>
  <div class="abs topbar-text" style="left:146px">Phone: +1 555 014 2207</div>
  <div class="abs topbar-text" style="left:800px">Request Demo</div>
  <div class="abs topbar-text" style="left:960px">Login</div>

  <nav>
    <div class="abs nav-link is-active" style="left:109px">Home</div>
    <div class="abs nav-link" style="left:196px">About Us</div>
    <div class="abs nav-link" style="left:303px">Services</div>
    <div class="abs nav-link" style="left:788px">Products</div>
    <div class="abs nav-link" style="left:905px">Gallery</div>
    <div class="abs nav-link" style="left:999px">Contact Us</div>
  </nav>
  <div class="abs brand"><span class="brand-mark"></span><span class="brand-name">R and P Orvex</span></div>

  <!-- hero -->
  <div class="ph hero-photo" role="img" aria-label="Worker in gloves cutting a steel tube with an angle grinder, sparks flying"></div>
  <svg class="abs" style="top:560px;left:0" width="1200" height="160" viewBox="0 0 1200 160" aria-hidden="true">
    <path d="M0,14 L600,100 L600,160 L0,160Z" fill="var(--blue)"/>
    <path d="M1200,4 L600,100 L600,160 L1200,160Z" fill="#9a9a9a"/>
    <path d="M0,60 Q600,150 1200,60 L1200,160 L0,160Z" fill="#fff"/>
  </svg>
  <div class="abs" style="top:664px;left:570px;width:60px;height:60px;border-radius:50%;background:#fff;box-shadow:0 2px 8px rgba(0,0,0,.2)"></div>

  <h1 class="abs hero-title">Engineering Flow,<br>Forming Future</h1>
  <p class="abs hero-text">At R&amp;P Orvex, we specialize in precision tube bending and subassembly manufacturing livering expert solutions across a diverse range of materials including mild steel, stainless steel, aluminum, and other non-ferrous metals.</p>
  <div class="btn" style="top:448px;left:101px;width:210px;height:50px">REQUEST A QUOTE
    <svg class="btn-hex" width="34" height="34" viewBox="0 0 34 34" aria-hidden="true"><polygon points="17,1 31,9 31,25 17,33 3,25 3,9" fill="#8b8b8b" stroke="#fff" stroke-width="2"/><path d="M12 22 L22 12 M15 12 H22 V19" stroke="#fff" stroke-width="2" fill="none"/></svg>
  </div>

  <!-- about -->
  <div class="ph about-band" role="img" aria-label="Blue-toned photo of stacked steel sheets"></div>
  <div class="abs about-card">
    <div class="ph about-photo" role="img" aria-label="Engineer in hard hat walking between large insulated pipelines"></div>
    <svg class="abs" style="top:208px;left:212px" width="64" height="64" viewBox="0 0 64 64" aria-hidden="true"><circle cx="32" cy="32" r="28" fill="#111" fill-opacity=".35" stroke="#fff" stroke-width="4"/><polygon points="25,19 46,32 25,45" fill="#fff"/></svg>
  </div>
  <h2 class="abs about-title">About Us</h2>
  <p class="abs about-sub">R&amp;P Orvex is a Perfect Fit for your Tube Bending needs!</p>
  <p class="abs about-tag">Engineering Flow, Forming Future</p>
  <p class="abs about-text">At R&amp;P Orvex, we specialize in precision tube bending and subassembly manufacturing, delivering expert solutions across a diverse range of materials including mild steel, stainless steel, aluminum, and other non-ferrous metals.</p>
  <div class="btn" style="top:1200px;left:649px;width:151px;height:51px">READ MORE
    <svg class="btn-hex" width="34" height="34" viewBox="0 0 34 34" aria-hidden="true"><polygon points="17,1 31,9 31,25 17,33 3,25 3,9" fill="#8b8b8b" stroke="#fff" stroke-width="2"/><path d="M12 22 L22 12 M15 12 H22 V19" stroke="#fff" stroke-width="2" fill="none"/></svg>
  </div>

  <!-- services -->
  <h2 class="abs center section-title services-title">Our <b>Services</b></h2>
  <p class="abs center services-text">We specialize in Tube and Pipe Bending We handle a variety of industrial projects with a wide scope of customer needs.<br>We offer custom bending solutions that are tailored to your unique needs.</p>

  <div class="abs service" style="left:93px">
    <svg width="120" height="118" viewBox="0 0 120 118" aria-hidden="true"><polygon points="60,3 114,31 114,87 60,115 6,87 6,31" fill="#8f8f8f" stroke="#fff" stroke-width="3"/><path d="M38 40h16v22h24v16M46 40v30h32M70 62v-12h12" stroke="#fff" stroke-width="3" fill="none"/></svg>
    <div class="service-name">Tube and Pipe Bending</div>
    <div class="service-text">We specialize in Tube and Pipe Bending We handle a variety of industrial</div>
  </div>
  <div class="abs service" style="left:350px">
    <svg width="120" height="118" viewBox="0 0 120 118" aria-hidden="true"><polygon points="60,3 114,31 114,87 60,115 6,87 6,31" fill="#8f8f8f" stroke="#fff" stroke-width="3"/><rect x="38" y="40" width="44" height="38" stroke="#fff" stroke-width="3" fill="none"/><path d="M38 52h44M50 52v26M60 52v26M70 52v26" stroke="#fff" stroke-width="3"/></svg>
    <div class="service-name">Tube End Forming</div>
    <div class="service-text">Our tube end forming service is second to none, providing precision</div>
  </div>
  <div class="abs service" style="left:608px">
    <svg width="120" height="118" viewBox="0 0 120 118" aria-hidden="true"><polygon points="60,3 114,31 114,87 60,115 6,87 6,31" fill="#8f8f8f" stroke="#fff" stroke-width="3"/><path d="M38 58 L60 38 L82 58 M44 54v26h32V54" stroke="#fff" stroke-width="3" fill="none"/><path d="M52 76c-4-6 4-8 0-14M60 76c-4-6 4-8 0-14M68 76c-4-6 4-8 0-14" stroke="#fff" stroke-width="2.5" fill="none"/></svg>
    <div class="service-name">Thermal Insulation</div>
    <div class="service-text">We offer comprehensive automotive insulation solutions</div>
  </div>
  <div class="abs service" style="left:864px">
    <svg width="120" height="118" viewBox="0 0 120 118" aria-hidden="true"><polygon points="60,3 114,31 114,87 60,115 6,87 6,31" fill="#8f8f8f" stroke="#fff" stroke-width="3"/><path d="M40 78 L54 64 M52 70 L74 48 L82 56 L60 78 Z M74 48 L80 40 L88 48 L82 56" stroke="#fff" stroke-width="3" fill="none"/></svg>
    <div class="service-name">Exhaust Muffler Silencers</div>
    <div class="service-text">Reducing noise and increasing comfort is our top priority</div>
  </div>

  <!-- products -->
  <h2 class="abs products-title">Our Products</h2>
  <div class="title-rule" style="top:2087px;left:111px;width:90px"></div>
  <svg class="abs" style="top:2053px;left:1021px" width="62" height="30" viewBox="0 0 62 30" aria-hidden="true"><circle cx="15" cy="15" r="12" fill="none" stroke="#222" stroke-width="1.5"/><path d="M18 9 L12 15 L18 21" stroke="#222" stroke-width="1.8" fill="none"/><circle cx="47" cy="15" r="12" fill="none" stroke="#222" stroke-width="1.5"/><path d="M44 9 L50 15 L44 21" stroke="#222" stroke-width="1.8" fill="none"/></svg>
  <div class="abs product-card"></div>
  <div class="ph product-img" style="left:130px;background:linear-gradient(135deg,#8e9499 0%,#d7dadc 40%,#6f757a 70%,#b9bec1 100%)" role="img" aria-label="Polished bent stainless steel tubes"></div>
  <div class="ph product-img" style="left:444px;background:linear-gradient(150deg,#6f7a8f 0%,#d4453d 35%,#c7322c 65%,#3a3f49 100%)" role="img" aria-label="Red tractor-mounted rotary mower frame built from formed tubes"></div>
  <div class="abs product-name" style="left:130px">Tube and Pipe Bending</div>
  <div class="abs product-name" style="left:444px">Tube End Forming</div>
  <div class="abs product-tab" style="left:777px"><span>Mild Steel</span></div>
  <div class="abs product-tab" style="left:886px"><span>Stainless Steel</span></div>
  <div class="abs product-tab" style="left:995px"><span>Aluminium</span></div>

  <!-- industries -->
  <div class="abs industries"></div>
  <h2 class="abs center section-title industries-title">Industries <b>We Serve</b></h2>
  <div class="title-rule" style="top:2775px;left:604px;width:46px;height:4px"></div>

  <div class="abs industry" style="left:111px">
    <div class="ph industry-img" style="background:linear-gradient(160deg,#9fb2cc 0%,#e8ecf1 50%,#5b79a8 100%)" role="img" aria-label="White safety helmet on construction blueprints"></div>
    <div class="industry-icon" style="background:var(--blue)"><svg width="30" height="30" viewBox="0 0 24 24" aria-hidden="true"><circle cx="12" cy="12" r="9" fill="none" stroke="#fff" stroke-width="2"/><path d="M8 12l3 3 5-6" stroke="#fff" stroke-width="2" fill="none"/></svg></div>
    <div class="industry-name">General Contracting</div>
    <div class="industry-rule"></div>
  </div>
  <div class="abs industry is-open" style="left:361px">
    <div class="ph industry-img" style="background:linear-gradient(170deg,#b9c3cc 0%,#8a97a3 50%,#c8cc8a 100%)" role="img" aria-label="Site team in hi-vis vests reviewing drawings inside a steel-frame building"></div>
    <div class="industry-icon" style="background:var(--grey)"><svg width="30" height="30" viewBox="0 0 24 24" aria-hidden="true"><path d="M4 14a8 8 0 0 1 16 0zM3 14h18v3H3zM12 6v8" stroke="#fff" stroke-width="2" fill="none"/></svg></div>
    <div class="industry-name">Design-Build<br>Construction</div>
    <div class="industry-text">Streamlined collaboration from concept to completion.</div>
  </div>
  <div class="abs industry" style="left:615px">
    <div class="ph industry-img" style="background:linear-gradient(160deg,#5a5a5a 0%,#9a9a9a 45%,#d8672b 60%,#444 100%)" role="img" aria-label="Rescue crew in orange suits working in rubble"></div>
    <div class="industry-icon" style="background:var(--blue)"><svg width="30" height="30" viewBox="0 0 24 24" aria-hidden="true"><path d="M4 20V10l8-6 8 6v10zM9 20v-6h6v6" stroke="#fff" stroke-width="2" fill="none"/></svg></div>
    <div class="industry-name">Disaster Recovery</div>
    <div class="industry-rule"></div>
  </div>
  <div class="abs industry" style="left:865px">
    <div class="ph industry-img" style="background:linear-gradient(170deg,#9fb6c9 0%,#c9cfd2 45%,#8d7d62 75%,#6a6455 100%)" role="img" aria-label="Workers on a shoreline cleanup site near industrial tanks"></div>
    <div class="industry-icon" style="background:var(--grey)"><svg width="30" height="30" viewBox="0 0 24 24" aria-hidden="true"><circle cx="12" cy="12" r="8" fill="none" stroke="#fff" stroke-width="2"/><circle cx="12" cy="12" r="3" fill="#fff"/></svg></div>
    <div class="industry-name">Environmental<br>Remediation</div>
    <div class="industry-rule"></div>
  </div>

  <!-- gallery -->
  <h2 class="abs center section-title gallery-title">Our <b>Gallery</b></h2>
  <div class="title-rule" style="top:3407px;left:570px;width:52px;height:4px"></div>
  <div class="ph gallery-img" style="left:0;width:70px;background:linear-gradient(160deg,#d8493c,#9e2a22)" role="img" aria-label="Red fabricated frame"></div>
  <div class="ph gallery-img" style="left:88px;width:333px;background:linear-gradient(160deg,#5d5a4a 0%,#e8c21d 35%,#d5ad12 70%,#6b5f2a 100%)" role="img" aria-label="Yellow welded steel mould frame"></div>
  <div class="ph gallery-img" style="left:436px;width:333px;background:linear-gradient(150deg,#5f6266 0%,#a7abaf 45%,#3c3f42 100%)" role="img" aria-label="Machined steel shafts on a workbench"></div>
  <div class="ph gallery-img" style="left:784px;width:333px;background:linear-gradient(160deg,#c9cccf 0%,#eceeef 50%,#9fa4a8 100%)" role="img" aria-label="Grey electrical control cabinets"></div>
  <div class="ph gallery-img" style="left:1131px;width:69px;background:linear-gradient(160deg,#c05a4a,#7a7a7a)" role="img" aria-label="Fabricated assembly"></div>
  <div class="gallery-arrow" style="left:41px"><svg width="20" height="20" viewBox="0 0 20 20" aria-hidden="true"><path d="M13 3 L6 10 L13 17" stroke="#333" stroke-width="1.8" fill="none"/></svg></div>
  <div class="gallery-arrow" style="left:1095px"><svg width="20" height="20" viewBox="0 0 20 20" aria-hidden="true"><path d="M7 3 L14 10 L7 17" stroke="#333" stroke-width="1.8" fill="none"/></svg></div>

  <!-- contact -->
  <div class="abs contact-bg"></div>
  <svg class="abs" style="top:3850px;left:0" width="1200" height="120" viewBox="0 0 1200 120" aria-hidden="true">
    <path d="M0,110 L600,2 L600,40 Q300,70 0,120Z" fill="var(--blue)"/>
    <path d="M1200,82 L600,2 L600,40 Q900,60 1200,100Z" fill="#8f8f8f"/>
    <path d="M0,120 Q300,70 600,40 Q900,60 1200,100 L1200,120Z" fill="#e6e7e9"/>
  </svg>
  <h2 class="abs center section-title contact-title"><b>Contact</b> Us</h2>
  <div class="title-rule" style="top:4000px;left:502px;width:120px;height:4px"></div>
  <div class="field" style="top:4040px;left:111px;width:461px;height:49px">Name</div>
  <div class="field" style="top:4110px;left:111px;width:461px;height:49px">Email</div>
  <div class="field" style="top:4178px;left:111px;width:461px;height:49px">Phone</div>
  <div class="field" style="top:4040px;left:591px;width:461px;height:258px">Message</div>
  <div class="btn submit">SUBMIT
    <svg class="btn-hex" width="34" height="34" viewBox="0 0 34 34" aria-hidden="true"><polygon points="17,1 31,9 31,25 17,33 3,25 3,9" fill="#8b8b8b" stroke="#fff" stroke-width="2"/><path d="M12 22 L22 12 M15 12 H22 V19" stroke="#fff" stroke-width="2" fill="none"/></svg>
  </div>

  <!-- footer -->
  <div class="abs footer-mark"></div>
  <div class="abs footer-brand">R and P Orvex</div>

  <div class="abs footer-head" style="left:333px">Other Links</div>
  <div class="abs footer-link" style="top:4535px;left:333px">FAQ</div>
  <div class="abs footer-link" style="top:4565px;left:333px">Terms of Use</div>
  <div class="abs footer-link" style="top:4595px;left:333px">Privacy Policy</div>
  <div class="abs footer-link" style="top:4627px;left:333px">Support Links</div>
  <div class="abs footer-link" style="top:4657px;left:333px">Conditions</div>

  <div class="abs footer-head" style="left:544px">Contact Us</div>
  <div class="abs contact-item" style="top:4543px;left:542px"><span class="contact-dot"><svg width="16" height="16" viewBox="0 0 24 24" aria-hidden="true"><path d="M12 2a7 7 0 0 0-7 7c0 5 7 13 7 13s7-8 7-13a7 7 0 0 0-7-7zm0 9.5A2.5 2.5 0 1 1 12 6.5a2.5 2.5 0 0 1 0 5z" fill="#fff"/></svg></span>Orvex Works, Pune, India</div>
  <div class="abs contact-item" style="top:4603px;left:542px"><span class="contact-dot"><svg width="16" height="16" viewBox="0 0 24 24" aria-hidden="true"><path d="M3 6h18v12H3zM3 6l9 7 9-7" stroke="#fff" stroke-width="2" fill="none"/></svg></span>hello@randporvex.in</div>
  <div class="abs contact-item" style="top:4663px;left:542px"><span class="contact-dot"><svg width="16" height="16" viewBox="0 0 24 24" aria-hidden="true"><path d="M6.6 10.8a15 15 0 0 0 6.6 6.6l2.2-2.2a1 1 0 0 1 1-.25 11.4 11.4 0 0 0 3.6.6 1 1 0 0 1 1 1V20a1 1 0 0 1-1 1A17 17 0 0 1 3 4a1 1 0 0 1 1-1h3.5a1 1 0 0 1 1 1c0 1.25.2 2.45.6 3.6a1 1 0 0 1-.25 1z" fill="#fff"/></svg></span>+1 555 014 2207</div>

  <div class="abs footer-head" style="left:863px">Sign Up To Our Newsletter</div>
  <p class="abs news-text">Lorem ipsum dolor sit amet,consectetur adipiscing elit,adipiscing elit.</p>
  <div class="abs news-email">Email</div>
  <div class="abs news-line"></div>
  <div class="btn subscribe">SUBSCRIBE
    <svg class="btn-hex" width="34" height="34" viewBox="0 0 34 34" aria-hidden="true"><polygon points="17,1 31,9 31,25 17,33 3,25 3,9" fill="#8b8b8b" stroke="#fff" stroke-width="2"/><path d="M12 22 L22 12 M15 12 H22 V19" stroke="#fff" stroke-width="2" fill="none"/></svg>
  </div>

  <div class="abs footer-rule"></div>
  <div class="abs center copyright">Copyrights@2026.R and P Orvex.All Rights Reserved</div>
</div>
</body>
</html>
```